Develop a PowerPoint template based on existing logo for a non-profit international alliance of professionals.
Presentations that will be made with this template will include mostly bullet point text and some tables. SOme images could also be included.

Target Market(s)

Governments, private funders

Industry/Entity Type

Non-Profit

Requirements
Must have
• clean and modern feel
Should not have
• no background in the slide area

```html
<!DOCTYPE html>
<html lang="en">
<head>
<meta charset="utf-8">
<title>Northbridge Alliance – Presentation Template</title>
<link rel="stylesheet" href="https://fonts.googleapis.com/css2?family=Audiowide&family=PT+Sans:wght@400;700&family=PT+Sans+Narrow:wght@700&display=swap">
<style>
  :root {
    --red: #e31f26;
    --red-dark: #b5141a;
    --pink: #ef8f93;
    --grey-dot: #7a7a7a;
    --black: #000000;
    --ink: #111111;
    --rule: #8a8a8a;
    --white: #ffffff;
    --cell-light: #f4f4f4;
    --cell-mid: #c4c4c4;
  }
  * { margin: 0; padding: 0; box-sizing: border-box; }
  html, body { width: 1200px; height: 918px; overflow: hidden; background: var(--white); }
  body { position: relative; font-family: "PT Sans", Arial, sans-serif; color: var(--ink); }

  .slide { position: absolute; width: 592px; height: 451px; overflow: hidden; background: var(--white); }
  .slide--cover   { left: 0;   top: 0; }
  .slide--section { left: 608px; top: 0; }
  .slide--content { left: 0;   top: 467px; }
  .slide--table   { left: 608px; top: 467px; }

  .footer-bar { position: absolute; left: 0; right: 0; bottom: 0; height: 18px; background: var(--black); }

  .brand { position: absolute; display: flex; align-items: center; gap: 5px;
           font-family: "PT Sans", Arial, sans-serif; font-weight: 700; color: var(--red); white-space: nowrap; }
  .brand__dot { border-radius: 50%; background: var(--red); flex: none; }
  .brand--large { left: 326px; top: 18px; font-size: 22px; }
  .brand--large .brand__dot { width: 26px; height: 26px; }
  .brand--small { font-size: 10px; gap: 3px; }
  .brand--small .brand__dot { width: 12px; height: 12px; }

  /* Cover */
  .cover__photo { position: absolute; left: 0; top: 0; width: 301px; height: 451px;
    background: linear-gradient(160deg, #5f8fcf 0%, #9fc0e6 25%, #8c97a4 50%, #37598f 75%, #b9ad97 100%); }
  .cover__bar { left: 301px; }
  .cover__title { position: absolute; left: 301px; right: 0; top: 93px; text-align: center;
    font-weight: 700; font-size: 14px; }

  /* Section */
  .section__heading { position: absolute; left: 0; right: 0; top: 4px; text-align: center;
    font-family: "Audiowide", sans-serif; font-size: 46px; font-weight: 400; color: var(--red); letter-spacing: 1px; }
  .section__art { position: absolute; left: 0; top: 90px; width: 290px; height: 343px;
    background: linear-gradient(180deg, #b9b9b9 0%, #d9d9d9 40%, #f4c3c5 70%, #f2b1b4 100%); }
  .section__number { position: absolute; left: 544px; top: 140px; width: 30px; height: 30px;
    border-radius: 50%; background: var(--black); color: var(--white); font-weight: 700; font-size: 17px;
    display: flex; align-items: center; justify-content: center; }
  .section__part { position: absolute; left: 402px; right: 0; top: 178px; height: 25px;
    background: var(--red); border-radius: 13px 0 0 13px; color: var(--white); font-weight: 700;
    font-size: 17px; line-height: 25px; text-align: right; padding-right: 10px; }
  .section .brand--small { left: 478px; top: 412px; }

  /* Content */
  .content__heading { position: absolute; left: 0; top: 84px; width: 296px; height: 25px;
    background: var(--red); border-radius: 0 13px 13px 0; color: var(--white); font-weight: 400;
    font-family: "Audiowide", sans-serif; font-size: 17px; line-height: 25px; text-align: right; padding-right: 14px; }
  .content__subheading { position: absolute; left: 415px; right: 0; top: 118px; height: 25px;
    background: var(--black); border-radius: 13px 0 0 13px; color: var(--white); font-weight: 400;
    font-family: "Audiowide", sans-serif; font-size: 12px; line-height: 25px; text-align: right; padding-right: 6px; }
  .content__column { position: absolute; top: 225px; width: 282px; border-top: 1px solid var(--rule);
    padding-top: 14px; font-weight: 700; font-size: 9.5px; line-height: 11.6px; }
  .content__column p + p { margin-top: 11px; }
  .content__column--left { left: 12px; }
  .content__column--right { left: 309px; width: 276px; }
  .content .brand--small { left: 8px; top: 410px; }

  /* Table */
  .table__title { position: absolute; left: 208px; width: 350px; text-align: center; top: 92px;
    font-family: "Audiowide", sans-serif; font-size: 28px; font-weight: 400; color: var(--red); }
  .data-table { position: absolute; left: 211px; top: 151px; border-collapse: separate; border-spacing: 8px 5px; margin: -5px -8px; }
  .data-table td { width: 167px; height: 33px; border-radius: 3px; text-align: center;
    font-family: "PT Sans Narrow", sans-serif; font-weight: 700; font-size: 13px; }
  .data-table .cell-label { background: linear-gradient(#ef3b40, var(--red) 45%, var(--red-dark)); color: var(--white); }
  .data-table .cell-figure { background: linear-gradient(90deg, var(--cell-light), var(--cell-mid)); color: var(--ink); border: 1px solid #d6d6d6; }
  .data-table .row--total .cell-label { background: linear-gradient(#5a5a5a, #1a1a1a 50%, #000); font-size: 15px; }
  .data-table .row--total .cell-figure { font-size: 15px; }
  .slide--table .brand--small { left: 478px; top: 410px; }
</style>
</head>
<body>

<section class="slide slide--cover">
  <div class="cover__photo" role="img" aria-label="Photograph of a modern glass office tower against a blue sky"></div>
  <div class="brand brand--large"><span class="brand__dot"></span>Northbridge Alliance</div>
  <h1 class="cover__title">Presentation Title</h1>
  <div class="footer-bar cover__bar"></div>
</section>

<section class="slide slide--section section">
  <h2 class="section__heading">HEADING</h2>
  <div class="section__art" role="img" aria-label="Decorative dotted ring pattern in grey and pink"></div>
  <div class="section__number">1</div>
  <div class="section__part">part A</div>
  <div class="brand brand--small"><span class="brand__dot"></span>Northbridge Alliance</div>
  <div class="footer-bar"></div>
</section>

<section class="slide slide--content content">
  <h2 class="content__heading">HEADING</h2>
  <h3 class="content__subheading">SUB-HEADING</h3>
  <div class="content__column content__column--left">
    <p>Lorem ipsum dolor sit amet, pellentesque mauris ligula magna ut. Mauris duis pretium, vitae in ad viverra, dictum placerat. Turpis nunc.Vestibulum est cras, donec in suscipit, vitae ut feugiat. Non maxime, ipsum suspendisse consectetuer. Donec id aliquam nulla arcu, orci inceptos metus molestie lorem quis, sed orci lacus, vestibulum sit. Aenean ut tellus volutpat, orci nec cum justo tortor, convallis lorem nostra ipsum eget. Imperdiet maecenas quis fermentum, eget donec felis mi orci justo aliquet. Lectus viverra donec nunc quam commodo, conubia risus. Vitae sagittis lacus ullamcorper sagittis nec ultricies, elit cursus consequat faucibus nam ac est. Tellus viverra, nostra integer, tellus mollis sint, in commodo eu ultrices, turpis facilisi ut velit. Wisi phasellus aliquam, ut</p>
  </div>
  <div class="content__column content__column--right">
    <p>Lorem ipsum dolor sit amet, pellentesque mauris ligula magna ut. Mauris duis pretium, vitae in ad viverra, dictum placerat. Turpis nunc.Vestibulum est cras, donec in suscipit, vitae ut feugiat. Non maxime, ipsum suspendisse consectetuer. Donec id aliquam nulla arcu, orci inceptos metus molestie lorem quis, sed orci lacus, vestibulum sit.</p>
    <p>Aenean ut tellus volutpat, orci nec cum justo tortor, convallis lorem nostra ipsum eget. Imperdiet maecenas quis fermentum, eget</p>
  </div>
  <div class="brand brand--small"><span class="brand__dot"></span>Northbridge Alliance</div>
  <div class="footer-bar"></div>
</section>

<section class="slide slide--table">
  <h2 class="table__title">TABLE</h2>
  <table class="data-table">
    <tr><td class="cell-label">Text Information</td><td class="cell-figure">Figures</td></tr>
    <tr><td class="cell-label">Text Information</td><td class="cell-figure">Figures</td></tr>
    <tr><td class="cell-label">Text Information</td><td class="cell-figure">Figures</td></tr>
    <tr><td class="cell-label">Text Information</td><td class="cell-figure">Figures</td></tr>
    <tr><td class="cell-label">Text Information</td><td class="cell-figure">Figures</td></tr>
    <tr class="row--total"><td class="cell-label">Text Information</td><td class="cell-figure">Figures</td></tr>
  </table>
  <div class="brand brand--small"><span class="brand__dot"></span>Northbridge Alliance</div>
  <div class="footer-bar"></div>
</section>

</body>
</html>
```